Bright Arc Electrical & Communications business card design

We would like a double sided business card that is different. Want it to be exciting and fun. Something that people keep rather then just throw it in the bin.
We have a logo that we want to put on one side of the business card and then the business information on the reverse side. Trying to go for a real professional style of business card

Target Market(s)

Electrical

Industry/Entity Type

Electrical

Contact Information for Business Card

Bright Arc Electrical & Communications
Marcus Trelowen
P: 0437 286 354
E: brightarc@mailrove.com.au
Lic No: 547106K
24/7

Font styles to use
Other font styles liked:
• Would like ideas

Requirements
Must have
• Our company logo (preferably on both sides) yellow needs to be incorporated somewhere. Business card card colours to match with logo. Maybe a small pop of colour
Nice to have
• Open to some design ideas

```html
<!DOCTYPE html>
<html lang="en">
<head>
<meta charset="utf-8">
<title>Bright Arc Electrical &amp; Communications – Business Card</title>
<link rel="stylesheet" href="https://fonts.googleapis.com/css2?family=Source+Sans+3:ital,wght@0,400;0,700;1,400&display=swap">
<style>
  :root {
    --card-bg: #ffffff;
    --ink: #000000;
  }
  html, body {
    margin: 0;
    padding: 0;
    width: 1200px;
    height: 777px;
    overflow: hidden;
    background: var(--card-bg);
  }
  .card {
    position: relative;
    width: 1200px;
    height: 777px;
    background: var(--card-bg);
    color: var(--ink);
    font-family: "Source Sans 3", "Myriad Pro", Arial, sans-serif;
    text-align: center;
  }
  .card__person {
    position: absolute;
    top: 167px;
    left: 0;
    width: 100%;
    margin: 0;
    font-size: 47px;
    font-style: italic;
    font-weight: 400;
    line-height: 50px;
    white-space: nowrap;
  }
  .card__company {
    position: absolute;
    top: 324px;
    left: 0;
    width: 100%;
    margin: 0;
    font-size: 55px;
    font-weight: 700;
    line-height: 60px;
    white-space: nowrap;
  }
  .card__contact {
    position: absolute;
    top: 405px;
    left: 0;
    width: 100%;
    margin: 0;
    padding: 0;
    list-style: none;
    font-size: 48px;
    font-weight: 400;
    line-height: 59px;
    white-space: nowrap;
  }
</style>
</head>
<body>
  <main class="card">
    <p class="card__person">Marcus Trelowen</p>
    <h1 class="card__company">Bright Arc Electrical &amp; Communications ltd</h1>
    <ul class="card__contact">
      <li class="card__phone">P: 0437 286 354</li>
      <li class="card__email">E: brightarc@mailrove.com.au</li>
      <li class="card__licence">Lic No: 547106K</li>
      <li class="card__hours">24/7</li>
    </ul>
  </main>
</body>
</html>
```